Cleaning service website design

We need a new nice web design(logo will be the same) for a new cleaning service Company:

Informations about Company and logo you can take from flyers in attachments.

This is a cleaning service Company which have simple rules and we would like to show that(in checklist form) on website:

- What we do and that we're Cleaning Green

- Why us?

- How much(our pricing is simple)

Also we would like to communicate with clients by some nice/big pictures on website and the most important thing is our phone number and short/fast Freestimate.

Also there should be some space for description about our Company.

Generally all information on main page can be short: about us, about service(what we do), last reviews, tips (for example: Tip of the week) and other can be some introduction to subpage where will be more information.

There will be few subpages like: About us, About our service, Photos(Before and after), Reviews , Tips, FAQ, Contact, Looking for a Job? - most of them will be just text so you can project just one example.

```html
<!DOCTYPE html>
<html lang="en">
<head>
<meta charset="utf-8">
<title>Tidy Nest House Cleaning</title>
<link rel="stylesheet" href="https://fonts.googleapis.com/css2?family=Roboto:wght@400;500;700&family=Roboto+Condensed:wght@400;700&family=Cinzel:wght@400&family=Kaushan+Script&family=Arimo:wght@400;700&display=swap">
<style>
:root{
  --sky-top:#2b7fd6;
  --sky-mid:#7bb6ec;
  --sky-low:#e6f1fb;
  --navy:#1d4f8c;
  --navy-dark:#143a6b;
  --blue-panel:#1667b8;
  --blue-panel-dark:#0f4f96;
  --green:#5fb845;
  --green-dark:#48a138;
  --green-light:#7fc870;
  --lime:#9bd21f;
  --lime-dark:#5e9a12;
  --white:#ffffff;
  --ink:#333333;
  --grey-text:#666666;
  --heading-blue:#2a72b5;
  --band:#efefef;
  --footer:#6b6b6b;
}
*{box-sizing:border-box;margin:0;padding:0}
html,body{width:1200px;height:1096px;overflow:hidden}
body{position:relative;font-family:"Arimo",Arial,sans-serif;color:var(--ink);
  background:linear-gradient(180deg,var(--sky-top) 0,var(--sky-mid) 260px,var(--sky-low) 560px,#ffffff 800px)}
.abs{position:absolute}

/* header */
.brand{left:52px;top:28px;width:220px}
.brand-mark{display:flex;align-items:center;gap:10px}
.brand-dot{width:44px;height:44px;border-radius:50%;background:var(--green)}
.brand-name{font-family:"Arimo",sans-serif;font-size:30px;font-weight:700;color:var(--white)}
.brand-tag{left:59px;top:104px;font-family:"Roboto Condensed",sans-serif;font-weight:700;font-size:22px;color:var(--white)}
.top-links{right:72px;top:9px;font-family:"Roboto",sans-serif;font-size:14px;font-weight:500;color:var(--white);word-spacing:2px}
.top-links span{margin:0 9px;color:#d8e8f8}
.top-call{right:75px;top:38px;color:var(--white);font-family:"Roboto",sans-serif}
.top-call small{font-size:20px;margin-right:6px}
.top-call strong{font-size:36px;font-weight:400}
.nav{top:97px;left:475px;display:flex;gap:7px}
.nav a{display:block;height:37px;line-height:37px;text-align:center;color:var(--white);text-decoration:none;
  font-family:"Roboto",sans-serif;font-weight:700;font-size:13px;border-radius:4px 4px 0 0;
  background:linear-gradient(180deg,#2d6bb0,var(--navy-dark));border:1px solid #5d8fc8;border-bottom:none}
.nav a.active{background:linear-gradient(180deg,#8fd14a,var(--green-dark));border-color:#a8dd7a}

.sheet{left:50px;top:133px;width:1080px;height:675px;background:var(--white);border-top:7px solid var(--green);border-radius:6px 6px 0 0}

/* hero */
.hero{left:59px;top:150px;width:705px;height:367px;border-radius:4px;overflow:hidden;
  background:linear-gradient(120deg,#d9c9a8 0%,#e8dccb 40%,#c7b79c 75%,#8a7560 100%)}
.hero-caption{left:0;bottom:0;width:100%;height:47px;background:rgba(40,40,40,.72);
  font-family:"Cinzel",serif;font-size:27px;color:var(--white);padding:6px 0 0 14px}

.promo{left:773px;top:148px;width:349px;height:370px;border-radius:6px;
  background:radial-gradient(circle at 60% 55%,#2a86d6,var(--blue-panel-dark));color:var(--white)}
.promo h2{position:absolute;left:19px;top:12px;font-family:"Roboto",sans-serif;font-weight:500;font-size:25px;color:#bfe0ff}
.promo ul{position:absolute;left:30px;top:55px;list-style:none;font-family:"Roboto",sans-serif;font-weight:700;font-size:14.5px;line-height:19px}
.promo li{display:flex;gap:6px;margin-bottom:9px}
.arrow{flex:none;width:16px;height:12px;margin-top:3px}
.promo-today{position:absolute;left:0;width:100%;top:209px;text-align:center;font-family:"Roboto",sans-serif;font-weight:500;font-size:20px;line-height:24px;color:#111}
.promo-phone{position:absolute;left:0;width:100%;top:233px;text-align:center;font-family:"Roboto",sans-serif;font-weight:700;font-size:40px;line-height:48px}
.promo-low{position:absolute;left:18px;top:288px;font-family:"Roboto",sans-serif;font-weight:700;font-size:16px;color:#cde8ff}
.promo-low b{font-size:48px;color:var(--lime);margin-left:2px;vertical-align:-6px}
.quote-btn{left:950px;top:437px;width:183px;height:51px;background:linear-gradient(180deg,#a9de3a,var(--lime-dark));
  clip-path:polygon(14px 0,100% 0,100% 100%,14px 100%,0 50%);color:var(--white);font-family:"Roboto Condensed",sans-serif;
  font-weight:700;font-size:29px;line-height:51px;padding-left:27px}

/* green cards */
.card{top:526px;width:349px;height:265px;border-radius:5px;background:var(--green-light);color:#1f1f1f;overflow:hidden}
.card-head{height:42px;background:var(--green);font-family:"Roboto Condensed",sans-serif;font-weight:700;font-size:20px;color:var(--white);padding:11px 0 0 16px}
.features{list-style:none;position:absolute;left:15px;top:59px;font-family:"Roboto",sans-serif;font-size:15px}
.features li{display:flex;gap:7px;height:32px}
.big-price{position:absolute;left:195px;top:108px;font-family:"Roboto",sans-serif;font-weight:700;font-size:74px;color:var(--white)}
.script{font-family:"Kaushan Script",cursive;font-weight:400;font-size:28px;color:#1b1b1b;margin-left:6px;vertical-align:-4px}
.price-row{position:absolute;left:21px;font-family:"Roboto Condensed",sans-serif;font-weight:700;font-size:14px}
.price-row b{font-size:31px;color:var(--white);margin-right:6px;font-weight:700}
.note{position:absolute;left:0;width:100%;top:221px;text-align:center;font-family:"Roboto Condensed",sans-serif;font-size:14px;color:var(--white)}
.field{position:absolute;background:linear-gradient(180deg,#fff,#f1f1f1);border-radius:3px;font-family:"Roboto",sans-serif;font-size:14px;color:#555;padding:9px 9px;box-shadow:0 1px 2px rgba(0,0,0,.25)}
.send{position:absolute;left:248px;top:171px;width:89px;height:56px;border-radius:4px;background:linear-gradient(180deg,#9fd43a,var(--lime-dark));
  color:var(--white);font-family:"Roboto Condensed",sans-serif;font-weight:700;font-size:24px;text-align:center;line-height:56px}

/* info band */
.band{left:0;top:808px;width:1200px;height:248px;background:var(--band)}
.col{top:825px}
.col h3{font-family:"Roboto",sans-serif;font-weight:400;font-size:23px;color:var(--heading-blue)}
.col p{font-size:13px;line-height:19.8px;color:var(--grey-text)}
.divider{top:826px;width:1px;height:212px;background:#d5d5d5}
.more{font-size:13px;color:var(--heading-blue);text-decoration:underline}
.thumb{position:absolute;border-radius:2px}
.tip h4{font-size:13px;font-weight:700;color:#333}
.tip p{font-size:12.5px;line-height:18px}

.footer{left:0;top:1056px;width:1200px;height:40px;background:var(--footer);color:var(--white);font-size:13px;padding:14px 0 0 51px}
.social{right:86px;top:1069px;display:flex;gap:8px}
.social span{width:17px;height:17px;border-radius:2px;background:#d9d9d9}
</style>
</head>
<body>

<header>
  <div class="abs brand"><div class="brand-mark"><span class="brand-dot"></span><span class="brand-name">Tidy Nest</span></div></div>
  <div class="abs brand-tag">house cleaning</div>
  <nav class="abs top-links">Reviews<span>|</span>Tips<span>|</span>FAQ<span>|</span>Looking for a Job?</nav>
  <div class="abs top-call"><small>Call Us</small><strong>555-014-2290</strong></div>
  <nav class="abs nav">
    <a class="active" style="width:123px">HOME</a>
    <a style="width:122px">ABOUT US</a>
    <a style="width:122px">OUR SERVICES</a>
    <a style="width:120px">GALLERY</a>
    <a style="width:123px">CONTACTUS</a>
  </nav>
</header>

<div class="abs sheet"></div>

<section class="abs hero" role="img" aria-label="Photo of a smiling family with their dog relaxing on a sofa in a clean living room">
  <div class="abs hero-caption">SIMPLIFY YOUR LIFE</div>
</section>

<section class="abs promo">
  <h2>What do we clean?</h2>
  <ul>
    <li><svg class="arrow" viewBox="0 0 16 12"><path d="M1 3c5 0 8 2 10 5l2-3 2 6-6-1 2-1.5C9 5.5 6 4.5 1 5z" fill="#8cc6ff"/></svg><span>Thoroughly clean your bathrooms,<br>kitchen,&nbsp; bedrooms and living areas</span></li>
    <li><svg class="arrow" viewBox="0 0 16 12"><path d="M1 3c5 0 8 2 10 5l2-3 2 6-6-1 2-1.5C9 5.5 6 4.5 1 5z" fill="#8cc6ff"/></svg><span>Mop or vacuum your floors</span></li>
    <li><svg class="arrow" viewBox="0 0 16 12"><path d="M1 3c5 0 8 2 10 5l2-3 2 6-6-1 2-1.5C9 5.5 6 4.5 1 5z" fill="#8cc6ff"/></svg><span>Dust surfaces</span></li>
    <li><svg class="arrow" viewBox="0 0 16 12"><path d="M1 3c5 0 8 2 10 5l2-3 2 6-6-1 2-1.5C9 5.5 6 4.5 1 5z" fill="#8cc6ff"/></svg><span>Collect garbage</span></li>
    <li><svg class="arrow" viewBox="0 0 16 12"><path d="M1 3c5 0 8 2 10 5l2-3 2 6-6-1 2-1.5C9 5.5 6 4.5 1 5z" fill="#8cc6ff"/></svg><span>Make beds</span></li>
  </ul>
  <div class="promo-today">Call Us Today!</div>
  <div class="promo-phone">555-014-2290</div>
  <div class="promo-low">as Low as<b>$79</b></div>
</section>
<div class="abs quote-btn">Get a quote</div>

<section class="abs card" style="left:58px">
  <div class="card-head">FULL HOUSE CLEANING ARE FROM</div>
  <ul class="features">
    <li><svg class="arrow" viewBox="0 0 16 12"><path d="M1 3c5 0 8 2 10 5l2-3 2 6-6-1 2-1.5C9 5.5 6 4.5 1 5z" fill="#fff"/></svg>Locally Owned &amp; Operated</li>
    <li><svg class="arrow" viewBox="0 0 16 12"><path d="M1 3c5 0 8 2 10 5l2-3 2 6-6-1 2-1.5C9 5.5 6 4.5 1 5z" fill="#fff"/></svg>Reliable &amp; Affordable</li>
    <li><svg class="arrow" viewBox="0 0 16 12"><path d="M1 3c5 0 8 2 10 5l2-3 2 6-6-1 2-1.5C9 5.5 6 4.5 1 5z" fill="#fff"/></svg>All Supplies Provided</li>
    <li><svg class="arrow" viewBox="0 0 16 12"><path d="M1 3c5 0 8 2 10 5l2-3 2 6-6-1 2-1.5C9 5.5 6 4.5 1 5z" fill="#fff"/></svg>Pet Friendly</li>
    <li><svg class="arrow" viewBox="0 0 16 12"><path d="M1 3c5 0 8 2 10 5l2-3 2 6-6-1 2-1.5C9 5.5 6 4.5 1 5z" fill="#fff"/></svg>No Contracts</li>
    <li><svg class="arrow" viewBox="0 0 16 12"><path d="M1 3c5 0 8 2 10 5l2-3 2 6-6-1 2-1.5C9 5.5 6 4.5 1 5z" fill="#fff"/></svg>Green Cleaning</li>
  </ul>
  <div class="big-price">$79</div>
</section>

<section class="abs card" style="left:416px">
  <div class="card-head">PRICING IS...<span class="script">simple</span></div>
  <div class="price-row" style="top:60px"><b>$79</b>for homes less than 1000 sq. ft.</div>
  <div class="price-row" style="top:112px"><b>$89</b>for homes 1000-1800 sq. ft.</div>
  <div class="price-row" style="top:164px"><b>$99</b>for homes 1800-2600 sq. ft.</div>
  <div class="note">*rates are for regular service*</div>
</section>

<section class="abs card" style="left:773px">
  <div class="card-head">QUICK FREESTIMATE</div>
  <div class="field" style="left:15px;top:66px;width:157px;height:36px">Name</div>
  <div class="field" style="left:181px;top:64px;width:157px;height:36px">Email</div>
  <div class="field" style="left:15px;top:118px;width:157px;height:36px">Phone</div>
  <div class="field" style="left:181px;top:118px;width:157px;height:36px">Address</div>
  <div class="field" style="left:15px;top:171px;width:223px;height:56px">Message</div>
  <div class="send">SEND</div>
</section>

<div class="abs band"></div>

<section class="abs col" style="left:58px;width:326px">
  <h3>About Us</h3>
  <p style="margin-top:11px;text-align:justify">Lorem Ipsum is simply dummy text of the printing and typesetting industry. Lorem Ipsum has been the industry's standard dummy text ever since the 1500s, when an unknown printer took a galley of type and scrambled it to make a type specimen book.&nbsp; industry's standard dummy text ever since the 1500s, when an unknown printer took a galley of type and scrambled it to make a type specimen book.</p>
  <a class="more abs" style="left:296px;top:201px">More</a>
</section>
<div class="abs divider" style="left:409px"></div>

<section class="abs col" style="left:420px;width:336px">
  <h3>Reviews</h3>
  <h4 style="font-size:13px;margin:12px 0 0 2px">Review Heading Topic</h4>
  <div class="thumb" style="left:4px;top:70px;width:103px;height:104px;background:linear-gradient(135deg,#ffffff,#e6e6e6 60%,#f3c9a8)" role="img" aria-label="Hand ticking a checklist box with a pen"></div>
  <p style="position:absolute;left:123px;top:68px;width:213px;text-align:justify;font-size:12.5px;line-height:17.8px">Lorem Ipsum is simply dummy text of the printing and typesetting industry. Lorem Ipsum has been the industry's standard dummy text ever since the 1500s, when an unmen book. It has survived not o</p>
  <a class="more abs" style="left:305px;top:201px">More</a>
</section>
<div class="abs divider" style="left:766px"></div>

<section class="abs col tip" style="left:776px;width:342px">
  <h3>Tip of the week</h3>
  <div class="thumb" style="left:7px;top:37px;width:69px;height:49px;background:linear-gradient(135deg,#9fcf6a,#e7c5a1 50%,#6aa0d8)" role="img" aria-label="Family photo outdoors"></div>
  <div style="position:absolute;left:87px;top:36px;width:248px">
    <h4>Heading</h4>
    <p>Lorem Ipsum is simply dummy text of the printing and typesetting industry. Lorem Ipsum has been the ..</p>
  </div>
  <div style="position:absolute;left:0;top:113px;width:342px;height:1px;background:#d8d8d8"></div>
  <div class="thumb" style="left:7px;top:127px;width:69px;height:49px;background:linear-gradient(180deg,#7fb8e8,#e2c19c 60%,#c9b07c)" role="img" aria-label="Family photo on the beach"></div>
  <div style="position:absolute;left:87px;top:126px;width:248px">
    <h4>Heading</h4>
    <p>Lorem Ipsum is simply dummy text of the printing and typesetting industry. Lorem Ipsum has been the ..</p>
  </div>
  <a class="more abs" style="left:312px;top:201px">More</a>
</section>

<footer class="abs footer">© 2012 Tidy Nest House Cleaning. All rights reserved.</footer>
<div class="abs social" aria-label="Social links"><span></span><span></span><span></span><span></span></div>

</body>
</html>
```